Course Graduation Certificate

This project is not for a flyer but instead for the creation of a course graduation certificate. The final certificate needs to include the Marlowe Summit Aviation Academy logo and the text stating as follows:
Certifies that ___________________________ has satisfactorily completed the course of _______________________________ on ________________________________
I would also like to include some type of gold seal of completion as well as a place to sign my name and credentials at the bottom of the certificate
I have included the Marlowe Summit Aviation Academy logo as well as three other certificate examples for you to work from.
Target Market(s)
Students completing a certification course and receiving a certificate
Look and feel

```html
<!DOCTYPE html>
<html lang="en">
<head>
<meta charset="utf-8">
<title>Graduation Certificate – Marlowe Summit Aviation Academy</title>
<link rel="stylesheet" href="https://fonts.googleapis.com/css2?family=Montserrat:wght@700;800&family=Arimo&family=Pinyon+Script&family=EB+Garamond&family=Tinos&display=swap">
<style>
  :root {
    --paper: #f2f0ea;
    --cobalt: #0a56a0;
    --gold: #b39566;
    --gold-text: #a98a5b;
    --navy: #16203a;
    --ink: #1c1c1c;
    --rule: #2a3150;
    --ghost: rgba(120, 120, 120, 0.08);
  }
  * { margin: 0; padding: 0; box-sizing: border-box; }
  html, body { width: 1200px; height: 789px; overflow: hidden; background: var(--paper); }
  .certificate { position: relative; width: 1200px; height: 789px; background: var(--paper); overflow: hidden; }
  .corner-bands { position: absolute; inset: 0; }
  .ghost-mark {
    position: absolute; left: 0; right: 0; top: 345px; text-align: center;
    font-family: "Montserrat", sans-serif; font-weight: 800; font-size: 120px;
    letter-spacing: 14px; color: var(--ghost); white-space: nowrap;
  }
  .academy-name {
    position: absolute; top: 86px; left: 0; right: 0; text-align: center;
    font-family: "Montserrat", sans-serif; font-weight: 800; font-size: 30px;
    line-height: 34px; letter-spacing: 2px; color: var(--cobalt);
  }
  .seal { position: absolute; left: 993px; top: 45px; width: 150px; height: 150px; }
  .title {
    position: absolute; top: 212px; left: 0; right: 0; text-align: center;
    font-family: "Montserrat", sans-serif; font-weight: 800; font-size: 45px;
    letter-spacing: 3px; color: var(--navy);
  }
  .lead {
    position: absolute; left: 0; right: 0; text-align: center;
    font-family: "Arimo", sans-serif; font-size: 20px; color: var(--ink);
    display: flex; justify-content: center; align-items: center; gap: 18px;
  }
  .lead::before, .lead::after { content: ""; width: 120px; height: 1px; background: var(--gold); }
  .lead-certifies { top: 292px; }
  .lead-completed { top: 428px; }
  .lead-completed::before, .lead-completed::after { width: 95px; }
  .lead-on { top: 540px; }
  .lead-on::before, .lead-on::after { width: 115px; }
  .field-line { position: absolute; height: 1px; background: var(--rule); }
  .recipient {
    position: absolute; top: 316px; left: 0; right: 0; text-align: center;
    font-family: "Pinyon Script", cursive; font-size: 66px; color: var(--gold-text);
  }
  .course {
    position: absolute; top: 455px; left: 0; right: 0; text-align: center;
    font-family: "EB Garamond", serif; font-size: 50px; color: var(--gold-text);
  }
  .date {
    position: absolute; top: 564px; left: 0; right: 0; text-align: center;
    font-family: "EB Garamond", serif; font-size: 30px; letter-spacing: 1px; color: var(--gold-text);
  }
  .signature { position: absolute; left: 466px; top: 632px; width: 250px; height: 80px;
    background: linear-gradient(90deg, rgba(30,80,160,0.18), rgba(30,80,160,0.05)); }
  .signatory {
    position: absolute; top: 728px; left: 0; right: 0; text-align: center;
    font-family: "Tinos", serif; font-size: 16px; line-height: 21px; color: var(--ink);
  }
</style>
</head>
<body>
<main class="certificate">
  <svg class="corner-bands" width="1200" height="789" viewBox="0 0 1200 789" aria-hidden="true">
    <polygon points="0,0 412,0 0,398" fill="var(--gold)"/>
    <polygon points="0,0 382,0 0,368" fill="var(--cobalt)"/>
    <polygon points="1200,414 1200,789 828,789" fill="var(--gold)"/>
    <polygon points="1200,438 1200,789 852,789" fill="var(--cobalt)"/>
  </svg>

  <div class="ghost-mark" aria-hidden="true">MARLOWE SUMMIT</div>

  <div class="academy-name">MARLOWE SUMMIT<br>AVIATION ACADEMY</div>

  <svg class="seal" viewBox="0 0 150 150" role="img" aria-label="Gold seal of completion">
    <defs>
      <radialGradient id="sealGold" cx="40%" cy="35%" r="70%">
        <stop offset="0" stop-color="#e6cf9c"/>
        <stop offset="0.6" stop-color="#c39d5f"/>
        <stop offset="1" stop-color="#9c7a43"/>
      </radialGradient>
    </defs>
    <circle cx="75" cy="75" r="73" fill="url(#sealGold)"/>
  </svg>

  <h1 class="title">GRADUATION CERTIFICATE</h1>

  <p class="lead lead-certifies">Certifies that</p>
  <p class="recipient">Owen Hartley</p>
  <div class="field-line" style="left:248px; width:715px; top:395px;"></div>

  <p class="lead lead-completed">has satisfactorily completed the course of</p>
  <p class="course">MS300 Differences Training</p>
  <div class="field-line" style="left:236px; width:730px; top:515px;"></div>

  <p class="lead lead-on">on</p>
  <p class="date">14/02/2025</p>
  <div class="field-line" style="left:235px; width:736px; top:598px;"></div>

  <div class="signature" role="img" aria-label="Handwritten signature of the center leader"></div>
  <div class="field-line" style="left:481px; width:232px; top:719px;"></div>
  <p class="signatory">Lucien Moreau<br>- Center Leader - Head of Operations</p>
</main>
</body>
</html>
```